Learning platform for primary and secondary schools needs a new design

We need to restyle the website: www.pennaboschetto.org.
We are developing new functionalities that will enable to turn the platform in an interactive e-learning center for teachers, parents and pupils. Our target is providing contents and learning methods for primary and secondary school.
We want to give a new structure to the homepage and all menu sections and to find a new design that facilitates users to orientate themselves. We love our main picture and we would like to emphasize it. We like our logo and we don't want to change it.
The homepage should fulfil three main tasks:
- welcome visitors;
- encourage visitors to explore three areas of free contents: learning (scopri), experimenting (esperimenti), cooking (ricette)
- convert visitors in logged users (users can register as teachers, parents or students).
We also need a new design for:
- log-in page,
- slideshow,
- galleries of pictures,
- blog page,
- newsletter.
If you have any questions, do not hesitate to contact me.
Good job!
Giulia
Updates
Hi guys,
First of all I'd like to say thanks to all designers that submitted their ideas.
Up to now I didn't find any design that really convinced me, that's why I decided to share with you a design idea that could make easier your job (please see again the project briefing). I can't wait to see your new designs!
Good job
Ciao
Giuliabetta
Hi guys,
I would like to thank you for all your wonderful design proposals. We have just launched a friends and family voting pool to help us in getting the final decision. We'll let you know the result as soon as possible within tomorrow.
Ciao
Giuliabetta
Target Market(s)
Italian teachers, parents and students attending primary and secondary school
Industry/Entity Type
Cooking
Look and feel
Each slider illustrates characteristics of the customer's brand and the style your logo design should communicate.

```html
<!DOCTYPE html>
<html lang="it">
<head>
<meta charset="utf-8">
<title>PennaBoschetto</title>
<link href="https://fonts.googleapis.com/css2?family=Kalam:wght@400;700&family=Luckiest+Guy&display=swap" rel="stylesheet">
<style>
:root{
  --cream:#fdf3b6;
  --cream-dark:#f6e79c;
  --orange:#f07c0c;
  --orange-text:#ee7a14;
  --brown:#7a3f07;
  --brown-text:#6b3a0a;
  --green:#9cc41b;
  --teal:#1fa6a8;
  --social-blue:#3b5aa0;
  --social-red:#c8343b;
  --ink:#1f1f1f;
  --white:#ffffff;
  --sky-top:#36a9e6;
  --sky-bottom:#cfe9f4;
  --ground:#c6a7ae;
  --stitch:#c9c2a4;
}
*{box-sizing:border-box;margin:0;padding:0}
html,body{width:670px;height:1200px;overflow:hidden}
body{position:relative;background:var(--cream);font-family:Arial,Helvetica,sans-serif;color:var(--ink)}
.abs{position:absolute}

/* header */
.site-header{left:0;top:0;width:670px;height:72px;background:var(--cream)}
.brand{left:88px;top:26px;display:flex;align-items:center;gap:5px;font-family:'Kalam',cursive;font-weight:700;font-size:14px;line-height:18px;color:var(--orange-text)}
.brand-dot{width:14px;height:14px;border-radius:50%;background:var(--orange-text)}
.account-btn{top:32px;height:17px;display:flex;align-items:center;gap:4px;padding-left:5px;color:var(--white);font-size:8px}
.account-btn svg{width:8px;height:8px}
.btn-login{left:427px;width:51px;background:var(--green)}
.btn-register{left:484px;width:51px;background:var(--teal)}
.social{top:32px;width:18px;height:17px}
.social-blue{left:541px;background:var(--social-blue)}
.social-red{left:564px;background:var(--social-red)}

/* navigation */
.main-nav{left:0;top:72px;width:670px;height:23px;background:var(--orange)}
.nav-item{top:0;height:23px;line-height:23px;color:var(--white);font-size:8.5px;white-space:nowrap}
.nav-item.active{left:88px;width:62px;text-align:center;background:var(--green)}
.nav-item .caret{font-size:6px;color:#b5540a;margin-left:1px}

/* hero */
.hero{left:0;top:95px;width:670px;height:385px;background:linear-gradient(180deg,var(--sky-top) 0%,var(--sky-bottom) 62%,var(--ground) 78%,#e8d4d2 100%)}
.hero-title{left:0;top:22px;width:670px;text-align:center;font-family:'Kalam',cursive;font-weight:400;font-size:23px;line-height:32px;color:var(--white)}
.hero-art{left:9px;top:76px;width:636px;height:262px;border-radius:4px;background:linear-gradient(180deg,#f6c27a 0%,#f19a4e 55%,#d9b5a8 100%);opacity:.85}

/* welcome */
.welcome{left:0;top:480px;width:670px;height:182px;background:var(--cream)}
.welcome-title{left:0;top:28px;width:670px;text-align:center;color:var(--orange-text);font-weight:400;line-height:28px}
.welcome-title .lead{font-family:'Luckiest Guy','Kalam',cursive;font-size:20px;letter-spacing:.5px}
.welcome-title .name{font-family:'Kalam',cursive;font-size:21px}
.welcome-text{left:130px;top:76px;width:410px;text-align:center;font-size:7px;line-height:9px}
.stitch{left:0;width:670px;height:0;border-top:2px dashed var(--stitch)}

/* features */
.features{left:0;top:673px;width:670px;height:267px;background:var(--brown)}
.feature-card{top:48px;width:132px;height:179px;background:var(--cream);text-align:center}
.feature-icon{margin:10px auto 0;width:30px;height:26px;border-radius:4px;background:var(--green)}
.feature-title{font-family:'Kalam',cursive;font-weight:400;font-size:21px;color:var(--orange-text);line-height:26px;margin-top:2px}
.feature-text{font-size:7px;line-height:9px;padding:0 9px}
.feature-btn{display:inline-block;margin-top:6px;background:var(--teal);color:var(--white);font-size:7.5px;padding:4px 7px}
.feature-ornament{margin:8px auto 0;width:106px;height:14px;border-radius:7px;background:linear-gradient(90deg,#b9d36a,#8a5a2a,#b9d36a)}

/* footer */
.footer-heading{top:982px;font-family:'Kalam',cursive;font-weight:700;font-size:15px;line-height:20px;color:var(--brown-text)}
.post{left:88px;width:165px}
.post-title{color:var(--orange-text);font-size:8.5px;line-height:11px}
.post-meta{font-size:5.5px;margin-top:5px}
.post-excerpt{font-size:5.5px;font-style:italic;margin-top:6px;line-height:8px}
.post-excerpt span{color:var(--orange-text);font-style:normal}
.post-divider{left:88px;top:1072px;width:165px;border-top:1px dashed #7a6a4a}
.quick-links{left:305px;top:1013px;list-style:none}
.quick-links li{font-size:8px;color:var(--orange-text);height:17.5px;display:flex;align-items:center;gap:6px}
.quick-links li::before{content:"";border-left:5px solid var(--brown-text);border-top:3px solid transparent;border-bottom:3px solid transparent}
.newsletter-label{left:438px;top:1016px;font-size:8.5px;color:var(--orange-text)}
.newsletter-field{left:438px;top:1039px;width:111px;height:20px;background:var(--cream-dark);border:1px solid #d8c98a;font-size:6.5px;line-height:18px;padding-left:5px}
.newsletter-submit{left:549px;top:1039px;width:33px;height:20px;background:var(--green);display:flex;align-items:center;justify-content:center}
.touch-divider{left:438px;top:1072px;width:144px;border-top:1px dashed #7a6a4a}
.footer-social{top:1083px;width:18px;height:17px}
.footer-brand{left:515px;top:1108px;display:flex;align-items:center;gap:4px;font-family:'Kalam',cursive;font-weight:700;font-size:12px;line-height:16px;color:var(--orange-text)}
.footer-brand .brand-dot{width:11px;height:11px}
.copyright{left:0;top:1176px;width:670px;height:24px;background:var(--orange);color:var(--white);font-size:7px;text-align:center;line-height:24px}
</style>
</head>
<body>

<header class="site-header abs">
  <div class="brand abs"><span class="brand-dot"></span>PennaBoschetto</div>
  <a class="account-btn btn-login abs">
    <svg viewBox="0 0 8 8"><rect x="1" y="3.5" width="6" height="4.5" fill="#fff"/><path d="M2.3 3.5V2.3a1.7 1.7 0 0 1 3.4 0v1.2" stroke="#fff" fill="none" stroke-width="1"/></svg>Login</a>
  <a class="account-btn btn-register abs">
    <svg viewBox="0 0 8 8"><rect x=".5" y="1" width="6" height="6.5" fill="none" stroke="#fff" stroke-width="1"/><path d="M3 5l4-4" stroke="#fff" stroke-width="1.2"/></svg>Register</a>
  <span class="social social-blue abs" aria-label="Social link"></span>
  <span class="social social-red abs" aria-label="Social link"></span>
</header>

<nav class="main-nav abs">
  <span class="nav-item active abs">Home</span>
  <span class="nav-item abs" style="left:171px">Scopri<span class="caret">▼</span></span>
  <span class="nav-item abs" style="left:235px">Esperimenti<span class="caret">▼</span></span>
  <span class="nav-item abs" style="left:317px">Ricette<span class="caret">▼</span></span>
  <span class="nav-item abs" style="left:385px">Glossario</span>
  <span class="nav-item abs" style="left:460px">Blog</span>
  <span class="nav-item abs" style="left:516px">Il Progetto<span class="caret">▼</span></span>
</nav>

<section class="hero abs">
  <h1 class="hero-title abs">PennaBoschetto, il gusto della conoscenza.</h1>
  <div class="hero-art abs" role="img" aria-label="Illustrated street of colourful Italian shop houses: fruit stand, bakery, dairy, butcher and fish shop, with clouds above"></div>
</section>

<section class="welcome abs">
  <h2 class="welcome-title abs"><span class="lead">WELCOME TO</span> <span class="name">PennaBoschetto</span></h2>
  <p class="welcome-text abs">Lorem ipsum dolor sit amet, consectetur adipiscing elit. Duis tincidunt nisl vestibulum, rutrum ligula at, congue mauris. Suspendisse ac felis eget eros dignissim consequat. Donec ornare ipsum vel urna sodales, vitae adipiscing ante vulputate. Nulla ut tempor augue. Aliquam vulputate purus eget lectus mollis, sit amet mollis ipsum dignissim. In vel sodales enim, sed ultricies libero. Curabitur erat est, pretium in facilisis eu, sodales eu eros. Aenean varius sem ac mi iaculis, eget accumsan mauris imperdiet. Nullam rhoncus faucibus libero ac scelerisque. Nam malesuada hendrerit lacus eu suscipit. Sed commodo nisi scelerisque odio pellentesque auctor. Cras dictum erat sit amet diam cursus, ut convallis libero aliquam.</p>
</section>
<div class="stitch abs" style="top:661px"></div>

<section class="features abs">
  <article class="feature-card abs" style="left:88px">
    <div class="feature-icon" role="img" aria-label="Open book icon"></div>
    <h3 class="feature-title">Scopri</h3>
    <p class="feature-text">Lorem ipsum dolor sit amet, consectetur adipiscing elit. Aliquam vel malesuada quam. Ut posuere ultrices nulla sit amet luctus. Morbi ante nisl,</p>
    <a class="feature-btn">Read More</a>
    <div class="feature-ornament" role="img" aria-label="Leafy vine ornament"></div>
  </article>
  <article class="feature-card abs" style="left:269px">
    <div class="feature-icon" role="img" aria-label="Cooking pot icon"></div>
    <h3 class="feature-title">Esperiment</h3>
    <p class="feature-text">Lorem ipsum dolor sit amet, consectetur adipiscing elit. Aliquam vel malesuada quam. Ut posuere ultrices nulla sit amet luctus. Morbi ante nisl,</p>
    <a class="feature-btn">Read More</a>
    <div class="feature-ornament" role="img" aria-label="Leafy vine ornament"></div>
  </article>
  <article class="feature-card abs" style="left:450px">
    <div class="feature-icon" role="img" aria-label="Recipe scroll icon"></div>
    <h3 class="feature-title">Ricette</h3>
    <p class="feature-text">Lorem ipsum dolor sit amet, consectetur adipiscing elit. Aliquam vel malesuada quam. Ut posuere ultrices nulla sit amet luctus. Morbi ante nisl,</p>
    <a class="feature-btn">Read More</a>
    <div class="feature-ornament" role="img" aria-label="Leafy vine ornament"></div>
  </article>
</section>
<div class="stitch abs" style="top:940px"></div>

<footer>
  <h4 class="footer-heading abs" style="left:88px">Our Recent Blogs</h4>
  <div class="post abs" style="top:1015px">
    <p class="post-title">Benvenuti nel sito demo di PennaBoschetto</p>
    <p class="post-meta">Scritto da Giuliabetta Ferrandi il 30 agosto 2013 .</p>
    <p class="post-excerpt">PennaBoschetto è un programma di scienza ed educazione alimentare in fase sperimentale. <span>Read More [...]</span></p>
  </div>
  <div class="post-divider abs"></div>
  <div class="post abs" style="top:1085px">
    <p class="post-title">Come nasce il progetto PennaBoschetto</p>
    <p class="post-meta">Scritto da Giuliabetta Ferrandi il 30 agosto 2013 .</p>
    <p class="post-excerpt">La curiosità apre ogni porta e ci guida verso le risposte alle nostre domande. Con questa idea nel 2011 <span>Read More [...]</span></p>
  </div>

  <h4 class="footer-heading abs" style="left:305px">Quick Links</h4>
  <ul class="quick-links abs">
    <li>Home</li><li>Scopri</li><li>Esperimenti</li><li>Ricette</li><li>Glossario</li><li>Blog</li><li>Il Progetto</li>
  </ul>

  <h4 class="footer-heading abs" style="left:438px">Get in Touch</h4>
  <p class="newsletter-label abs">Signup for our Newsletter &amp; updates</p>
  <div class="newsletter-field abs">info@esempiostudio.com</div>
  <div class="newsletter-submit abs"><svg width="12" height="12" viewBox="0 0 12 12"><path d="M3 1.5 8 6 3 10.5" stroke="#fff" stroke-width="2.6" fill="none"/></svg></div>
  <div class="touch-divider abs"></div>
  <span class="footer-social social-blue abs" style="left:440px" aria-label="Social link"></span>
  <span class="footer-social social-red abs" style="left:463px" aria-label="Social link"></span>
  <div class="footer-brand abs"><span class="brand-dot"></span>PennaBoschetto</div>

  <div class="stitch abs" style="top:1166px"></div>
  <div class="copyright abs">Copyright © 2014 PennaBoschetto.</div>
</footer>

</body>
</html>
```